Harbor Crest Real Estate Business Cards

Looking to create a template for the agents in my office. The images below are an example of our current card, logos, and tagline. The requirements are:
1. Needs to include photo of agent
2. Needs to include Logo
3. Needs to include tag line. (current card doesn't include tagline.)
4. Needs to include phone, address, email, website and social media logos i.e. Find me at "f", "twitter (logo)" etc.
5. Need front and back design.
6. I don't want the old style safe style of business card. I want it to stand out in a stack of cards.
7. Do not make it look anything like what i currently have. This needs to be all new.
Thank you for your time.
Industry/Entity Type
Real Estate Agent
Contact Information for Business Card
I need name, address, email, website (www.pinevalleyhomefinder.example) social media logos
Requirements
Must have
- 1. Needs to include photo of agent
- 2. Needs to include Logo
- 3. Needs to include tag line. (current card doesn't include tagline.)
- 4. Needs to include phone, address, email, website and social media logos i.e. Find me at "f", "twitter (logo)" etc.
- 5. Need front and back design.
- 6. I don't want the old style safe style of business card. I want it to stand out in a stack of cards.
- 7. Do not make it look anything like what i currently have. This needs to be all new.
Should not have
- Not boring or plain.

```html
<!DOCTYPE html>
<html lang="en">
<head>
<meta charset="utf-8">
<title>Harbor Crest Real Estate – Business Cards</title>
<link href="https://fonts.googleapis.com/css2?family=Lato:wght@300;400;700;900&display=swap" rel="stylesheet">
<style>
  :root {
    --stage: #262626;
    --ink: #1c1c1c;
    --red: #d0202f;
    --white: #f6f7f8;
    --grey: #6e6e6e;
    --grey-light: #9a9a9a;
    --ring: #b9b6b0;
  }
  * { margin: 0; padding: 0; box-sizing: border-box; }
  html, body { width: 1200px; height: 900px; overflow: hidden; }
  body {
    background: var(--stage);
    font-family: "Lato", sans-serif;
    position: relative;
  }
  .card {
    position: absolute;
    left: 320px;
    width: 560px;
    height: 320px;
    overflow: hidden;
    box-shadow: 0 14px 30px rgba(0,0,0,.45);
  }

  /* ---------- Back ---------- */
  .card-back { top: 95px; background: var(--ink); }
  .card-back .rule-top {
    position: absolute; left: 300px; top: 72px; width: 240px; height: 2px; background: var(--red);
  }
  .card-back .rule-bottom {
    position: absolute; left: 20px; top: 246px; width: 226px; height: 2px; background: var(--red);
  }
  .card-back .brand {
    position: absolute; left: 70px; top: 112px; width: 170px;
    color: var(--grey); font-weight: 900; font-size: 27px; line-height: 1;
    text-transform: uppercase; text-align: right; letter-spacing: -0.5px;
  }
  .card-back .brand small {
    display: block; font-size: 12px; letter-spacing: 3px; margin-top: 6px; font-weight: 900;
  }
  .card-back .divider {
    position: absolute; left: 258px; top: 100px; width: 1px; height: 90px; background: var(--grey);
  }
  .card-back .tagline {
    position: absolute; left: 276px; top: 104px;
    font-weight: 300; font-size: 21px; line-height: 1.32; color: var(--grey);
  }
  .tagline em { font-style: normal; color: var(--red); text-transform: uppercase; }
  .card-back .social {
    position: absolute; left: 256px; top: 232px; display: flex; gap: 14px;
  }
  .social .social-box {
    width: 30px; height: 30px; border: 2px solid var(--red);
  }
  .card-back .handle {
    position: absolute; left: 0; right: 0; top: 276px; text-align: center;
    color: var(--grey); font-weight: 700; font-size: 19px;
    padding-left: 34px;
  }

  /* ---------- Front ---------- */
  .card-front { top: 485px; background: var(--white); }
  .card-front .panel { position: absolute; inset: 0; }
  .card-front .agent {
    position: absolute; left: 36px; top: 70px;
  }
  .agent .name { color: var(--red); font-weight: 900; font-size: 24px; line-height: 1.1; }
  .agent .role { color: var(--grey-light); font-weight: 400; font-size: 17px; margin-top: 2px; }
  .card-front .contacts {
    position: absolute; left: 36px; top: 170px; list-style: none;
    color: #fff; font-size: 14.5px; line-height: 23px;
  }
  .contacts li { display: flex; align-items: flex-start; gap: 10px; }
  .contacts svg { width: 13px; height: 13px; margin-top: 5px; flex: none; fill: #fff; }
  .contacts .address { line-height: 21px; }
  .card-front .photo {
    position: absolute; left: 380px; top: 24px; width: 150px; height: 150px;
    border-radius: 50%; border: 5px solid var(--ring);
    box-shadow: 0 0 0 2px #444;
    background: radial-gradient(circle at 50% 40%, #c8c8c8 0%, #8f8f8f 60%, #3a3d44 100%);
  }
  .card-front .brand {
    position: absolute; right: 22px; top: 196px; text-align: right;
    color: #4a4a4a; font-weight: 900; font-size: 26px; line-height: 1;
    text-transform: uppercase; letter-spacing: -0.5px;
  }
  .card-front .brand small { display: block; font-size: 11px; letter-spacing: 3px; margin-top: 4px; }
  .card-front .tagline {
    position: absolute; right: 22px; top: 260px; font-size: 12.5px; font-weight: 400; color: #4a4a4a;
  }
</style>
</head>
<body>

  <section class="card card-back" aria-label="Business card back">
    <div class="rule-top"></div>
    <div class="brand">Harbor Crest<small>Real Estate</small></div>
    <div class="divider"></div>
    <p class="tagline">Open <em>Doors</em><br>Fresh <em>Starts</em><br>True <em>Roots</em></p>
    <div class="social" aria-label="Social media">
      <span class="social-box"></span>
      <span class="social-box"></span>
    </div>
    <div class="rule-bottom"></div>
    <p class="handle">HarborCrest</p>
  </section>

  <section class="card card-front" aria-label="Business card front">
    <svg class="panel" width="560" height="320" viewBox="0 0 560 320">
      <polygon points="0,0 350,0 300,320 0,320" fill="var(--red)"/>
      <polygon points="0,58 345,58 331,150 0,150" fill="var(--ink)"/>
    </svg>
    <div class="agent">
      <p class="name">Daniel Whitaker</p>
      <p class="role">CEO</p>
    </div>
    <ul class="contacts">
      <li><svg viewBox="0 0 16 16"><path d="M3.5 1l3 3-1.6 1.8a9 9 0 0 0 5.3 5.3L12 9.5l3 3L13 15C6.5 14.5 1.5 9.5 1 3z"/></svg>012 555 0147</li>
      <li><svg viewBox="0 0 16 16"><path d="M1 3h14v10H1zM1.8 3.6 8 8.6l6.2-5" stroke="#d0202f" stroke-width="1.3"/></svg>hello@harborcrest.example</li>
      <li><svg viewBox="0 0 16 16"><circle cx="8" cy="8" r="6.5" fill="none" stroke="#fff" stroke-width="1.5"/><path d="M1.5 8h13M8 1.5c-3 3.5-3 9.5 0 13M8 1.5c3 3.5 3 9.5 0 13" fill="none" stroke="#fff" stroke-width="1.2"/></svg>www.pinevalleyhomefinder.example</li>
      <li class="address"><svg viewBox="0 0 16 16"><path d="M8 1a5 5 0 0 0-5 5c0 4 5 9 5 9s5-5 5-9a5 5 0 0 0-5-5zm0 7a2 2 0 1 1 0-4 2 2 0 0 1 0 4z"/></svg><span>4810 Harbor Lane 12<br>Street, Crestview</span></li>
    </ul>
    <div class="photo" role="img" aria-label="Portrait photo of the agent"></div>
    <div class="brand">Harbor Crest<small>Real Estate</small></div>
    <p class="tagline">Open <em>Doors</em> Fresh <em>Starts</em> True <em>Roots</em></p>
  </section>

</body>
</html>
```